Business Cards for IT Consulting Company (Managed Service Provider)

I am looking to have some business cards printed and would like some designs. We are an IT Consulting company based in Vancouver BC. I would like a nice clean and modern look to the cards. I have uploaded all the versions of my logo so parts can be used as needed. Here is a snippit from our website homepage:

Kelbrin Systems Ltd. is an IT Solutions Partner located in Vancouver BC, Canada. We offer IT solutions and support to customers in the greater Vancouver Area. With expertise in Quillara platforms, as well as Tovex and Bryn ZPL and over 12 years experience in the IT industry, Kelbrin Systems is dedicated to offering our clients top quality service and products. We take pride in the solutions we offer our customers. The greatest compliment a client can give us is to recommend our services.

Kelbrin Systems Ltd. offers a wide range of IT services from onsite service to remote support and managed service solutions. This allows clients to choose the support path that best suits their company’s needs. Supporting many different sized companies from small to enterprise level over the past 12 years Kelbrin Systems has the experience and expertise needed to ensure things run smoothly. Allowing our clients to focus on doing business.

Revolutionizing the way IT services are delivered.

Kelbrin Systems is dedicated to providing our clients with IT solutions that work and grow with them for years to come. This philosophy helps save money in the long run instead of replacing equipment constantly. Far too often IT solutions are not well thought out and while possibly solving the problem at hand, require replacement due to growth or quality within a very short time frame. Kelbrin Systems takes pride in providing solutions that will last and be able to accommodate growth without the need for replacement.

Industry/Entity Type

Information Technology

Contact Information for Business Card

Kelbrin Systems Ltd.
(Employee Name)
Eml: (Employees Email Address)
Web: kelbrinsys.me
Ph: 604-555-0142

Font styles to use
Serif
Sans Serif

Requirements
Must have
• The Company logo and company colors.
Nice to have
• - Our tag line: "Revolutionizing IT Services" or "Revolutionizing the way IT services are delivered."
• - Also I really like the idea of nature and technology together blending which is sort of where my logo came from so integrating that somehow onto the business cards would be great.

```html
<!DOCTYPE html>
<html lang="en">
<head>
<meta charset="utf-8">
<title>Kelbrin Systems Ltd. — Business Cards</title>
<link rel="stylesheet" href="https://fonts.googleapis.com/css2?family=Raleway:wght@300;400;500;700&display=swap">
<style>
  :root {
    --bg: #bfe6da;
    --card: #ffffff;
    --brand-blue: #1a9ad9;
    --ink-grey: #4a4a4a;
    --ink-dark: #222222;
    --panel-black: #0b0b0b;
    --shadow: rgba(30, 80, 70, 0.18);
  }
  * { box-sizing: border-box; margin: 0; padding: 0; }
  html, body {
    width: 1200px; height: 856px; overflow: hidden;
    background: var(--bg);
    font-family: "Raleway", Arial, sans-serif;
  }
  .sheet {
    position: relative; width: 1200px; height: 856px;
    display: flex; align-items: center; justify-content: center; gap: 48px;
  }
  .card {
    position: relative; width: 540px; height: 308px;
    background: var(--card); border-radius: 22px; overflow: hidden;
    box-shadow: 0 14px 30px var(--shadow);
  }

  /* Wordmark stand-in */
  .brand {
    display: flex; align-items: center; gap: 12px;
    color: var(--brand-blue); font-weight: 700; letter-spacing: 0.5px;
  }
  .brand-square {
    display: inline-block; background: var(--brand-blue); border-radius: 3px;
  }

  /* Front */
  .card-front {
    display: flex; flex-direction: column; align-items: center; justify-content: center; gap: 44px;
  }
  .card-front .brand { font-size: 36px; }
  .card-front .brand-square { width: 30px; height: 30px; }
  .tagline { font-size: 25px; font-weight: 400; color: var(--brand-blue); }
  .tagline .tagline-end { color: var(--ink-dark); }

  /* Back */
  .pattern-panel {
    position: absolute; left: 0; top: 0; bottom: 0; width: 212px;
    background: linear-gradient(135deg, var(--panel-black) 0%, #10222c 45%, #0d4f73 70%, var(--panel-black) 100%);
  }
  .contact-block {
    position: absolute; left: 240px; right: 24px; top: 30px;
  }
  .card-back .brand { font-size: 22px; gap: 9px; }
  .card-back .brand-square { width: 18px; height: 18px; }
  .person-name {
    margin-top: 30px; font-size: 28px; font-weight: 300; letter-spacing: 1px;
    color: var(--brand-blue); text-transform: uppercase;
  }
  .contact-list { list-style: none; margin-top: 22px; display: flex; flex-direction: column; gap: 14px; }
  .contact-item { display: flex; align-items: center; gap: 12px; font-size: 17px; color: var(--ink-dark); }
  .contact-icon {
    width: 26px; height: 26px; border-radius: 50%; background: var(--brand-blue);
    display: flex; align-items: center; justify-content: center; flex: none;
  }
  .contact-icon svg { width: 15px; height: 15px; }
</style>
</head>
<body>
<main class="sheet">

  <section class="card card-back" aria-label="Business card, contact side">
    <div class="pattern-panel" role="img" aria-label="Large black and blue geometric brand pattern"></div>
    <div class="contact-block">
      <div class="brand"><span class="brand-square"></span>Kelbrin Systems Ltd.</div>
      <h1 class="person-name">Dara Wexley</h1>
      <ul class="contact-list">
        <li class="contact-item">
          <span class="contact-icon">
            <svg viewBox="0 0 24 24" fill="#fff"><path d="M6.6 10.8a15.1 15.1 0 0 0 6.6 6.6l2.2-2.2c.3-.3.7-.4 1-.2 1.1.4 2.3.6 3.6.6.6 0 1 .4 1 1V20c0 .6-.4 1-1 1A17 17 0 0 1 3 4c0-.6.4-1 1-1h3.5c.6 0 1 .4 1 1 0 1.3.2 2.5.6 3.6.1.3 0 .7-.2 1z"/></svg>
          </span>
          dara.wexley@kelbrinsys.me
        </li>
        <li class="contact-item">
          <span class="contact-icon">
            <svg viewBox="0 0 24 24" fill="none" stroke="#fff" stroke-width="2"><rect x="3" y="6" width="18" height="12" rx="1"/><path d="M3 6l9 7 9-7"/></svg>
          </span>
          kelbrinsys.me
        </li>
        <li class="contact-item">
          <span class="contact-icon">
            <svg viewBox="0 0 24 24" fill="none" stroke="#fff" stroke-width="1.8"><circle cx="12" cy="12" r="9"/><path d="M3 12h18M12 3c3 3 3 15 0 18M12 3c-3 3-3 15 0 18"/></svg>
          </span>
          604-555-0142
        </li>
      </ul>
    </div>
  </section>

  <section class="card card-front" aria-label="Business card, brand side">
    <div class="brand"><span class="brand-square"></span>Kelbrin Systems Ltd.</div>
    <p class="tagline">Revolutionizing <span class="tagline-end">IT Services</span></p>
  </section>

</main>
</body>
</html>
```